Flyer für Kampfsport und Selbstverteidigung
Zielgruppe
Kampfsportschule für Kinder/Jugendliche und Erwachsene
Martial Arts Wenk
Flyerbeispiel finden Sie im Anhang
Aufgabenstellung
Es soll modern gestaltet sein und mit den Farben: Schwarz, Grau, weiß und rot gearbeitet werden.
Im Anhang ist mein alter Flyer. Der soll als Beispiel für Inhalt und Stil sein.

```html
<!DOCTYPE html>
<html lang="de">
<head>
<meta charset="utf-8">
<title>Martial Arts Wenk – Flyer</title>
<link href="https://fonts.googleapis.com/css2?family=Poppins:wght@600;700;800&family=Jost:wght@300;400&display=swap" rel="stylesheet">
<style>
  :root{
    --stage:#5b1517;
    --ink:#141213;
    --ink-soft:#241e1f;
    --red:#c4262b;
    --red-dark:#7d1619;
    --red-deep:#4a1b1b;
    --white:#ffffff;
    --grey:#d9d4d4;
    --line:#3a3233;
  }
  *{box-sizing:border-box;margin:0;padding:0}
  html,body{width:1200px;height:800px;overflow:hidden}
  body{background:var(--stage);font-family:"Jost",sans-serif;color:var(--white);position:relative}

  .flyer{position:absolute;top:30px;width:520px;height:740px;overflow:hidden;
    background:linear-gradient(165deg,var(--red-deep) 0%,var(--ink) 55%,var(--ink) 100%);
    box-shadow:0 20px 40px rgba(0,0,0,.45)}
  .flyer--front{left:50px}
  .flyer--back{left:630px}
  .flyer__shapes{position:absolute;inset:0}

  .headline{position:absolute;left:0;right:0;text-align:center;font-family:"Poppins",sans-serif;
    font-weight:800;text-transform:uppercase;letter-spacing:.5px;text-shadow:2px 3px 4px rgba(0,0,0,.6)}
  .subline{position:absolute;left:0;right:0;text-align:center;font-family:"Poppins",sans-serif;
    font-weight:700;color:var(--red);text-shadow:1px 2px 3px rgba(0,0,0,.5)}

  /* front */
  .flyer--front .headline{top:48px;font-size:42px}
  .flyer--front .subline{top:100px;font-size:22px}
  .hero-photo{position:absolute;left:190px;top:165px;width:300px;height:420px;border-radius:6px;
    background:radial-gradient(ellipse at 60% 40%,rgba(226,70,110,.55),rgba(30,20,22,.2) 70%)}
  .disciplines{position:absolute;left:40px;top:390px}
  .disciplines__title{font-family:"Poppins",sans-serif;font-weight:700;font-size:22px;margin-bottom:6px}
  .disciplines__list{list-style:none;font-size:17px;line-height:1.45}
  .disciplines__list li::before{content:"> "}
  .address{position:absolute;left:300px;top:592px;font-size:14px;line-height:1.4;color:var(--grey)}
  .brand{position:absolute;display:flex;align-items:center;gap:8px;font-family:"Poppins",sans-serif;
    font-weight:700;color:var(--white)}
  .brand__dot{width:14px;height:14px;border-radius:50%;background:var(--red)}
  .flyer--front .brand{left:36px;top:670px;font-size:17px}
  .contact{position:absolute;font-family:"Poppins",sans-serif}
  .contact__title{font-weight:700;font-size:17px;margin-bottom:8px}
  .contact__row{display:flex;align-items:center;gap:8px;font-size:12px;font-weight:600;margin-bottom:6px}
  .contact__row svg{flex:none}
  .flyer--front .contact{left:300px;top:654px}

  /* back */
  .flyer--back .headline{top:44px;font-size:40px}
  .flyer--back .subline{top:96px;font-size:22px}
  .schedule{position:absolute;left:20px;top:150px;width:480px;border-collapse:collapse;font-size:12px;line-height:1.2}
  .schedule th{background:var(--red);font-family:"Poppins",sans-serif;font-weight:700;font-size:13px;
    text-align:left;padding:6px 6px;border-right:1px solid var(--red-dark)}
  .schedule td{height:46px;padding:4px 6px;vertical-align:middle;color:var(--grey);
    border:1px solid var(--line);background:rgba(20,18,19,.35)}
  .schedule col.time{width:60px}
  .kid-photo{position:absolute;right:40px;top:455px;width:170px;height:275px;border-radius:6px;
    background:linear-gradient(180deg,rgba(240,236,236,.55),rgba(200,190,190,.25) 70%,rgba(230,190,40,.2))}
  .flyer--back .brand{left:70px;top:520px;font-size:22px}
  .flyer--back .contact{left:40px;top:610px}
  .flyer--back .contact__title{font-size:20px;margin-bottom:12px}
  .flyer--back .contact__row{font-size:13px;margin-bottom:10px}
</style>
</head>
<body>

<section class="flyer flyer--front">
  <svg class="flyer__shapes" viewBox="0 0 520 740" aria-hidden="true">
    <path d="M0 430 L260 170 Q300 130 340 170 L200 360 L0 620 Z" fill="var(--red-dark)"/>
    <path d="M40 560 L380 150 Q420 110 460 150 L120 620 Z" fill="var(--red)" opacity=".85"/>
    <path d="M0 740 L520 260 L520 740 Z" fill="var(--ink)"/>
    <circle cx="430" cy="700" r="190" fill="var(--ink-soft)"/>
    <line x1="20" y1="470" x2="60" y2="420" stroke="var(--red)" stroke-width="6"/>
  </svg>
  <h1 class="headline">Martial Arts Wenk</h1>
  <p class="subline">Kampfsport &amp; Selbstverteidigung</p>
  <div class="hero-photo" role="img" aria-label="Foto: Kind mit Kopfschutz, Boxhandschuhen und gelbem Gürtel beim hohen Seitwärtskick"></div>
  <div class="disciplines">
    <h2 class="disciplines__title">Disziplinen:</h2>
    <ul class="disciplines__list">
      <li>Kick-Boxen/Sportkarate</li>
      <li>Jiu-Jitsu Selbstverteidigung</li>
      <li>Tricking</li>
      <li>Ü25 Kick-Boxen</li>
    </ul>
  </div>
  <p class="address">Leitung: Timo Wenk<br>Am Werkhof 7<br>26400 Nordstadt</p>
  <div class="brand"><span class="brand__dot"></span>Martial Arts Wenk</div>
  <div class="contact">
    <p class="contact__title">Info &amp; Probetraining</p>
    <p class="contact__row">
      <svg width="16" height="12" viewBox="0 0 16 12"><rect x="1" y="1" width="14" height="10" fill="none" stroke="#fff" stroke-width="1.4"/><path d="M1 1 L8 7 L15 1" fill="none" stroke="#fff" stroke-width="1.4"/></svg>
      info@martial-arts-wenk.de</p>
    <p class="contact__row">
      <svg width="14" height="14" viewBox="0 0 14 14"><path d="M3 1 L5 1 L6 4 L4.5 5.5 Q6 8.5 8.5 9.5 L10 8 L13 9 L13 11 Q12 13 10 13 Q2 11 1 3 Q1 1 3 1 Z" fill="#fff"/></svg>
      0151 / 23456789</p>
  </div>
</section>

<section class="flyer flyer--back">
  <svg class="flyer__shapes" viewBox="0 0 520 740" aria-hidden="true">
    <path d="M0 560 L520 200 L520 740 L0 740 Z" fill="var(--ink)"/>
    <path d="M0 440 L300 260 L0 560 Z" fill="var(--red-dark)" opacity=".7"/>
    <circle cx="290" cy="740" r="210" fill="var(--ink-soft)"/>
  </svg>
  <h1 class="headline">Trainingsplan</h1>
  <p class="subline">Martial Arts Wenk</p>
  <table class="schedule">
    <colgroup><col class="time"><col><col><col><col><col></colgroup>
    <thead>
      <tr><th>Zeit</th><th>Montag</th><th>Dienstag</th><th>Mittwoch</th><th>Donnerstag</th><th>Freitag</th></tr>
    </thead>
    <tbody>
      <tr><td>15:00<br>15:45</td><td>Kick-Boxen<br>3-5 Jahre</td><td>Jiu-Jitsu<br>3-6 Jahre</td><td>Kick-Boxen<br>3-5 Jahre</td><td>Jiu-Jitsu<br>3-6 Jahre</td><td></td></tr>
      <tr><td>16:00<br>16:45</td><td>Kick-Boxen<br>6-7 Jahre</td><td>Jiu-Jitsu<br>7-12 Jahre</td><td>Kick-Boxen<br>6-7 Jahre</td><td>Jiu-Jitsu<br>7-12 Jahre</td><td></td></tr>
      <tr><td>17:00<br>17:45</td><td>Kick-Boxen<br>8-10 Jahre</td><td>Tricking<br>ab 6 Jahren</td><td>Kick-Boxen<br>8-10 Jahre</td><td>Tricking<br>ab 6 Jahren</td><td>Kick-Boxen<br>3-6 Jahre</td></tr>
      <tr><td>18:00<br>19:00</td><td>Kick-Boxen<br>10-12 Jahre</td><td>Kick-Boxen<br>Ü25 Gruppe</td><td>Kick-Boxen<br>10-12 Jahre</td><td>Kick-Boxen<br>Ü25 Gruppe</td><td>Kick-Boxen<br>ab 7 Jahren<br>ab Gelbgurt</td></tr>
      <tr><td>19:00<br>20:00</td><td></td><td></td><td>Kick-Boxen<br>ab 13 Jahren</td><td></td><td></td></tr>
    </tbody>
  </table>
  <div class="kid-photo" role="img" aria-label="Foto: Kind im weißen Kampfanzug mit gelbem Gürtel in Kampfhaltung"></div>
  <div class="brand"><span class="brand__dot"></span>Martial Arts Wenk</div>
  <div class="contact">
    <p class="contact__title">Info &amp; Probetraining</p>
    <p class="contact__row">
      <svg width="18" height="13" viewBox="0 0 16 12"><rect x="1" y="1" width="14" height="10" fill="none" stroke="#fff" stroke-width="1.4"/><path d="M1 1 L8 7 L15 1" fill="none" stroke="#fff" stroke-width="1.4"/></svg>
      info@martial-arts-wenk.de</p>
    <p class="contact__row">
      <svg width="16" height="16" viewBox="0 0 14 14"><path d="M3 1 L5 1 L6 4 L4.5 5.5 Q6 8.5 8.5 9.5 L10 8 L13 9 L13 11 Q12 13 10 13 Q2 11 1 3 Q1 1 3 1 Z" fill="#fff"/></svg>
      0151 / 23456789</p>
  </div>
</section>

</body>
</html>
```